Local Roofing/Construction company business needs new biz card design

We need a new business card design, current cards are from the start of this operation and generic at best. We are a local Construction Company (General Contractor) with a majority of our work originating from insurance claims-exterior finish work is the main focus (Roofs-Siding-Gutters etc). Heavily involved with homeowners and the low ball offers they receive from insurance company's after a insurable event takes place. I have attached some of our original logo file(s) below.

```html
<!DOCTYPE html>
<html lang="en">
<head>
<meta charset="utf-8">
<title>Ridgeline Builders – Business Card</title>
<link rel="stylesheet" href="https://fonts.googleapis.com/css2?family=Play:wght@400;700&display=swap">
<style>
  :root {
    --brand-green: #32d77a;
    --brand-green-faint: #e8f9ef;
    --ink: #1e1e1e;
    --card-white: #ffffff;
    --backdrop: #e6e6e6;
  }
  * { box-sizing: border-box; margin: 0; padding: 0; }
  html, body {
    width: 1093px;
    height: 1200px;
    overflow: hidden;
    background: var(--backdrop);
    font-family: "Play", sans-serif;
    color: var(--ink);
  }
  .canvas { position: relative; width: 1093px; height: 1200px; }

  .card {
    position: absolute;
    left: 264px;
    width: 580px;
    height: 356px;
    background: var(--card-white);
    border-radius: 36px;
    overflow: hidden;
  }
  .card--front { top: 226px; }
  .card--back { top: 621px; }

  /* Front */
  .accent-bar {
    position: absolute;
    left: 50px; top: 0;
    width: 26px; height: 184px;
    background: var(--brand-green);
  }
  .watermark-block {
    position: absolute;
    left: 304px; top: 172px;
    width: 266px; height: 200px;
    background: var(--brand-green-faint);
    border-radius: 8px;
  }
  .identity {
    position: absolute;
    right: 52px; top: 52px;
    text-align right;
    text-align: right;
  }
  .identity__name {
    font-weight: 700;
    font-size: 23px;
    line-height: 26px;
    letter-spacing: 0.5px;
    color: var(--brand-green);
  }
  .identity__title {
    font-size: 17px;
    line-height: 20px;
  }
  .identity-icon {
    position: absolute;
    left: 538px; top: 53px;
    width: 42px; height: 40px;
    background: var(--brand-green);
    display: flex; align-items: center; justify-content: center;
  }
  .contact-list { list-style: none; }
  .contact-item {
    position: absolute;
    left: 50px;
    display: flex;
    align-items: flex-start;
    font-size: 17px;
    line-height: 21px;
    white-space: nowrap;
  }
  .contact-item__icon {
    width: 25px; height: 23px;
    border-radius: 3px;
    background: var(--brand-green);
    display: flex; align-items: center; justify-content: center;
    flex-shrink: 0;
    margin-right: 9px;
  }
  .contact-item__text { padding-top: 1px; }
  .contact-item--phone { top: 191px; }
  .contact-item--email { top: 220px; }
  .contact-item--web { top: 247px; }
  .contact-item--address { top: 286px; }
  .highlight { color: var(--brand-green); }

  /* Back */
  .brand {
    position: absolute;
    left: 0; right: 0; top: 126px;
    display: flex; align-items: center; justify-content: center;
    gap: 14px;
  }
  .brand__square {
    width: 40px; height: 40px;
    background: var(--brand-green);
  }
  .brand__name {
    font-weight: 700;
    font-size: 36px;
    line-height: 40px;
    color: var(--brand-green);
    letter-spacing: 1px;
  }
  .base-band {
    position: absolute;
    left: 0; right: 0; bottom: 0;
    height: 18px;
    background: var(--brand-green);
  }
</style>
</head>
<body>
<main class="canvas">
  <section class="card card--front" aria-label="Business card front">
    <div class="accent-bar"></div>
    <div class="watermark-block" aria-hidden="true"></div>

    <div class="identity">
      <p class="identity__name">DANIEL HARPER</p>
      <p class="identity__title">Managing Director</p>
    </div>
    <div class="identity-icon">
      <svg width="20" height="22" viewBox="0 0 20 22" fill="#fff" aria-hidden="true">
        <circle cx="10" cy="6" r="5"/>
        <path d="M1 21c0-5 4-8 9-8s9 3 9 8z"/>
      </svg>
    </div>

    <ul class="contact-list">
      <li class="contact-item contact-item--phone">
        <span class="contact-item__icon">
          <svg width="15" height="15" viewBox="0 0 24 24" fill="none" stroke="#fff" stroke-width="2" aria-hidden="true">
            <path d="M5 3h4l2 5-2.5 1.5a11 11 0 0 0 6 6L16 13l5 2v4a2 2 0 0 1-2 2A17 17 0 0 1 3 5a2 2 0 0 1 2-2z"/>
            <path d="M15 3a6 6 0 0 1 6 6M15 7a2 2 0 0 1 2 2"/>
          </svg>
        </span>
        <span class="contact-item__text">055-318 204 672</span>
      </li>
      <li class="contact-item contact-item--email">
        <span class="contact-item__icon">
          <svg width="16" height="12" viewBox="0 0 16 12" fill="none" stroke="#fff" stroke-width="1.2" aria-hidden="true">
            <rect x="0.6" y="0.6" width="14.8" height="10.8"/>
            <path d="M0.6 0.6 8 7l7.4-6.4M0.6 11.4l5.6-5.6M15.4 11.4 9.8 5.8"/>
          </svg>
        </span>
        <span class="contact-item__text">info@ridgeline.com</span>
      </li>
      <li class="contact-item contact-item--web">
        <span class="contact-item__icon">
          <svg width="15" height="15" viewBox="0 0 16 16" fill="none" stroke="#fff" stroke-width="1.1" aria-hidden="true">
            <circle cx="8" cy="8" r="7"/>
            <ellipse cx="8" cy="8" rx="3" ry="7"/>
            <path d="M1 8h14M2 4.5h12M2 11.5h12"/>
          </svg>
        </span>
        <span class="contact-item__text">www.<span class="highlight">ridgelinebld</span>.com</span>
      </li>
      <li class="contact-item contact-item--address">
        <span class="contact-item__icon">
          <svg width="12" height="16" viewBox="0 0 12 16" fill="#fff" aria-hidden="true">
            <path d="M6 0a6 6 0 0 1 6 6c0 4-6 10-6 10S0 10 0 6a6 6 0 0 1 6-6zm0 3.5a2.5 2.5 0 1 0 0 5 2.5 2.5 0 0 0 0-5z"/>
          </svg>
        </span>
        <span class="contact-item__text">318, Cedar Hollow Road<br>60417,Brookfield</span>
      </li>
    </ul>
  </section>

  <section class="card card--back" aria-label="Business card back">
    <div class="brand">
      <span class="brand__square" aria-hidden="true"></span>
      <span class="brand__name">RIDGELINE BUILDERS</span>
    </div>
    <div class="base-band"></div>
  </section>
</main>
</body>
</html>
```